New letter head for Air Conditioning business

We need a new professional letter head design to suit our new re-branded air conditioning business. Our new logo is attached

```html
<!DOCTYPE html>
<html lang="en">
<head>
<meta charset="utf-8">
<title>Nordvale Air Conditioning &amp; Refrigeration – Letterhead</title>
<link rel="stylesheet" href="https://fonts.googleapis.com/css2?family=Arimo:wght@400;700&family=Dancing+Script:wght@500&display=swap">
<style>
  :root {
    --backdrop: #e8e4d6;
    --paper: #f6f6f7;
    --ink: #2b2b2e;
    --ink-soft: #3a3a3d;
    --brand-red: #cf4b43;
    --brand-green: #4ea26b;
    --brand-dark: #2e2e33;
  }
  * { box-sizing: border-box; margin: 0; padding: 0; }
  html, body {
    width: 1200px; height: 1012px; overflow: hidden;
    background: var(--backdrop);
    font-family: "Arimo", Arial, sans-serif;
    color: var(--ink);
  }
  .letterhead {
    position: absolute; left: 264px; top: 26px;
    width: 672px; height: 960px;
    background: var(--paper);
    box-shadow: 0 14px 40px rgba(60, 50, 20, 0.25);
    overflow: hidden;
  }
  .brand {
    position: absolute; left: 45px; top: 88px;
    display: flex; align-items: center; gap: 10px;
  }
  .brand-dot {
    width: 22px; height: 22px; border-radius: 50%;
    background: var(--brand-green);
  }
  .brand-name {
    font-size: 30px; font-weight: 700; letter-spacing: 2px;
    color: var(--brand-dark);
  }
  .header-rule {
    position: absolute; left: 328px; top: 48px;
    width: 2px; height: 104px; background: var(--brand-green);
  }
  .contact {
    position: absolute; left: 347px; top: 54px;
    list-style: none; font-size: 12.5px; color: var(--ink-soft);
  }
  .contact li { display: flex; align-items: center; height: 26.5px; }
  .contact li:first-child { padding-left: 0; }
  .contact svg { width: 15px; height: 15px; margin-right: 9px; flex: none; }
  .letter-body {
    position: absolute; left: 45px; top: 189px; width: 576px;
    font-size: 12.6px; line-height: 16px; color: var(--ink);
  }
  .letter-body p { margin-bottom: 16px; }
  .letter-body .salutation { margin-bottom: 26px; }
  .sign-off { margin-bottom: 20px; }
  .signature {
    font-family: "Dancing Script", cursive;
    font-size: 22px; line-height: 22px; color: var(--ink);
  }
  .signatory-role { margin-top: 0; }
  .footer-band {
    position: absolute; left: 0; bottom: 0; width: 672px; height: 36px;
  }
</style>
</head>
<body>
  <main class="letterhead">
    <div class="brand">
      <span class="brand-dot"></span>
      <span class="brand-name">NORDVALE</span>
    </div>

    <div class="header-rule"></div>

    <ul class="contact">
      <li>Nordvale Air Conditioning &amp; Refrigeration Address</li>
      <li>
        <svg viewBox="0 0 16 16" aria-hidden="true"><path fill="var(--brand-red)" d="M3.6 1.2 5.8 3.6c.4.4.4 1 0 1.4L4.7 6.1c.9 2 2.5 3.6 4.4 4.5l1.1-1.1c.4-.4 1-.4 1.4 0l2.4 2.2c.4.4.4 1 0 1.4l-1.3 1.3c-.6.6-1.5.8-2.3.5C6.3 13.3 2.7 9.7 1.1 5.6.8 4.8 1 3.9 1.6 3.3L2.9 2c.2-.5.4-.8.7-.8z"/></svg>
        +60 3210 4455
      </li>
      <li>
        <svg viewBox="0 0 16 16" aria-hidden="true"><rect x="1.5" y="3.5" width="13" height="9" fill="none" stroke="var(--brand-red)" stroke-width="1.4"/><path d="M1.5 3.5 8 9l6.5-5.5M1.5 12.5 6 8M14.5 12.5 10 8" fill="none" stroke="var(--brand-red)" stroke-width="1.2"/></svg>
        hello@nordvaleaircon .com
      </li>
      <li>
        <svg viewBox="0 0 16 16" aria-hidden="true"><g fill="none" stroke="var(--brand-red)" stroke-width="1.2"><circle cx="8" cy="8" r="6.5"/><ellipse cx="8" cy="8" rx="2.8" ry="6.5"/><path d="M1.5 8h13M2.6 4.6h10.8M2.6 11.4h10.8"/></g></svg>
        www.nordvaleaircon .com
      </li>
    </ul>

    <section class="letter-body">
      <p class="salutation">Lorem Ipsum,</p>
      <p>Lorem ipsum dolor sit amet, consectetur adipiscing elit, sed do eiusmod tempor incididunt ut labore et dolore magna aliqua. Sed viverra tellus in hac habitasse platea. Quisque non tellus orci ac auctor. Ut venenatis tellus in metus vulputate.</p>
      <p>Lacus vestibulum sed arcu non odio euismod lacinia at. Posuere lorem ipsum dolor sit amet consectetur adipiscing. Consequat ac felis donec et odio pellentesque. Et leo duis ut diam quam nulla porttitor massa. Purus semper eget duis at. In eu mi bibendum neque. Pulvinar etiam non quam lacus suspendisse faucibus interdum posuere. Nisl pretium fusce id velit ut tortor. Enim praesent elementum facilisis leo vel fringilla est. Odio pellentesque diam volutpat commodo sed egestas egestas. Diam quis enim lobortis scelerisque fermentum. Odio facilisis mauris sit amet massa vitae. Purus faucibus ornare suspendisse sed. Viverra orci sagittis eu volutpat odio facilisis mauris.</p>
      <p>Ridiculus mus mauris vitae ultricies leo integer malesuada. Id cursus metus aliquam eleifend. Euismod elementum nisi quis eleifend. Sem viverra aliquet eget sit. Eu ultrices vitae auctor eu augue ut lectus arcu. Malesuada bibendum arcu vitae elementum curabitur. A arcu cursus vitae congue mauris rhoncus aenean vel elit. Quam elementum pulvinar etiam non. Pellentesque pulvinar pellentesque habitant morbi tristique senectus et. Dignissim cras tincidunt lobortis feugiat vivamus at augue. Morbi blandit cursus risus at. Sagittis eu volutpat odio facilisis mauris. Habitasse platea dictumst quisque sagittis purus sit amet volutpat. Faucibus interdum posuere lorem ipsum dolor sit amet consectetur adipiscing. Nulla pharetra diam sit amet nisl suscipit.</p>
      <p>Lorem ipsum dolor sit amet, consectetur adipiscing elit, sed do eiusmod tempor incididunt ut labore et dolore magna aliqua. Sed viverra tellus in hac habitasse platea. Quisque non tellus orci ac auctor. Ut venenatis tellus in metus vulputate.</p>
      <p class="sign-off">Regards</p>
      <div class="signature">Your name</div>
      <div class="signatory-role">Company Director</div>
    </section>

    <svg class="footer-band" viewBox="0 0 672 36" preserveAspectRatio="none" aria-hidden="true">
      <polygon points="0,0 400,0 436,36 0,36" fill="var(--brand-red)"/>
      <polygon points="404,0 672,0 672,36 440,36" fill="var(--paper)"/>
      <polygon points="410,0 672,0 672,36 446,36" fill="var(--brand-green)"/>
    </svg>
  </main>
</body>
</html>
```